Brand Consulting Website, Simple Design/Layout that nails the "less is more" approach t...

I have an account on Quillbase through Tarnlink, so the design will need to be built there. I already have a logo, and the design of the website should at least compliment the look of the logo. The placeholder website where the logo can be seen is at www.valdromeconsulting.example. The purpose of the website at this point in time is not to drive business, but rather, to have a strong appearance and add some credibility to my already existing business.

The website should have some level of abstraction about it. I prefefer designs and shapes of images of people. The fewer people, the better. No stock photography of people standing around talking to each other.

Requirements
Must have
• The ability to work on my existing Quill Base Account
Should not have
• Stock photography of people standing around doing "business-y" stuff. That is sooo old and played out, and is the opposite of the type of message I am trying to portray.

```html
<!DOCTYPE html>
<html lang="en">
<head>
<meta charset="utf-8">
<title>Valdrome – A Specialized Brand Consultancy</title>
<link rel="stylesheet" href="https://fonts.googleapis.com/css2?family=Montserrat:wght@400;500;600;700&display=swap">
<style>
:root{
  --orange:#f15a22;
  --orange-deep:#e0480f;
  --charcoal:#4a4a4a;
  --charcoal-dark:#3b3b3b;
  --ink:#2e2e2e;
  --white:#ffffff;
  --muted:#d8d8d8;
}
*{box-sizing:border-box;margin:0;padding:0}
html,body{width:1200px;height:4675px;overflow:hidden}
body{background:var(--charcoal);font-family:'Montserrat',sans-serif;color:var(--white);position:relative}
.abs{position:absolute}
.btn{display:inline-flex;align-items:center;gap:8px;background:var(--orange);color:var(--white);font-weight:700;text-transform:uppercase;text-decoration:none}
.section-title{font-size:36px;font-weight:400;text-transform:uppercase;text-align:center;letter-spacing:1px}
.lede{font-size:15px;line-height:32px;text-align:center;color:var(--muted)}

/* header */
.site-header{left:0;top:0;width:1200px;height:118px;background:var(--charcoal)}
.support{left:92px;top:30px;display:flex;align-items:center;gap:14px}
.support-icon{width:44px;height:44px;border-radius:50%;border:3px solid var(--orange);display:flex;align-items:center;justify-content:center}
.support-label{font-size:14px;color:var(--orange);font-weight:600}
.support-number{font-size:26px;font-weight:700}
.brand{left:445px;top:12px;display:flex;align-items:center;gap:14px}
.brand-square{width:86px;height:86px;background:var(--white)}
.brand-name{font-size:46px;font-weight:500;color:var(--orange);letter-spacing:1px}
.header-cta{left:848px;top:31px;height:54px;padding:0 26px;border-radius:27px;font-size:15px}
.main-nav{left:0;top:118px;width:1200px;height:62px;background:var(--orange);display:flex;justify-content:center;align-items:center;gap:46px}
.main-nav a{color:var(--white);text-decoration:none;font-size:17px;font-weight:500;text-transform:uppercase}

/* hero */
.hero{left:0;top:180px;width:1200px;height:600px}
.hero-photo{position:absolute;inset:0;background:linear-gradient(110deg,#6f5a44 0%,#8a8f93 35%,#b9b6ae 65%,#5a5e63 100%)}
.hero-copy{right:90px;top:140px;width:560px;text-align:right}
.hero-copy h1{font-size:54px;font-weight:400;letter-spacing:1px}
.hero-copy h2{font-size:28px;font-weight:700;margin-top:6px}
.hero-copy p{font-size:17px;line-height:34px;margin-top:14px}
.hero-cta{margin-top:22px;height:56px;padding:0 26px;border-radius:28px;font-size:15px}

/* about */
.about-visual{left:112px;top:880px;width:436px;height:436px;border-radius:50%;border:8px solid var(--orange);background:radial-gradient(circle,#ffffff 0%,#e9e9e9 70%,#cfcfcf 100%);box-shadow:0 0 0 6px var(--white)}
.about-copy{left:583px;top:948px;width:526px}
.about-copy h2{font-size:36px;font-weight:400;text-transform:uppercase;letter-spacing:1px}
.about-copy p{font-size:15px;line-height:32px;color:var(--muted);text-align:justify;margin-top:14px}
.about-cta{margin-top:24px;height:42px;padding:0 22px;font-size:16px}

/* services */
.services{left:0;top:1435px;width:1200px;height:690px}
.services-photo{position:absolute;inset:0;background:linear-gradient(180deg,#2c2c2c 0%,#3f3f3f 50%,#555 100%)}
.services .section-title{position:absolute;left:0;top:130px;width:1200px}
.services .lede{position:absolute;left:190px;top:185px;width:820px}
.service-card{top:1708px;width:320px;height:256px;background:rgba(95,95,95,.82);text-align:center;padding-top:16px}
.service-card h3{font-size:19px;font-weight:500;color:var(--orange);text-transform:uppercase;margin-top:10px}
.service-card p{font-size:13px;line-height:27px;color:var(--white);margin:8px 22px 0}
.service-card .more{display:block;font-size:14px;font-weight:700;color:var(--orange);margin-top:6px;text-transform:uppercase}
.slider-arrow{width:44px;height:30px}

/* approach */
.approach-title{left:0;top:2205px;width:1200px}
.approach-lede{left:140px;top:2255px;width:920px}
.step{top:2420px;width:240px;text-align:center}
.step-ring{width:234px;height:234px;border-radius:50%;border:3px solid var(--orange);padding:14px;margin:0 auto}
.step-ring div{width:100%;height:100%;border-radius:50%;border:14px solid var(--orange);background:var(--charcoal-dark);display:flex;align-items:center;justify-content:center}
.step-label{font-size:22px;text-transform:uppercase;margin-top:30px}

/* testimonials */
.testimonials{left:0;top:2810px;width:1200px;height:680px}
.testimonials-photo{position:absolute;inset:0;background:linear-gradient(160deg,#3a3a3a 0%,#6c6c6c 45%,#9a8f86 80%,#5d5347 100%)}
.testimonials .section-title{position:absolute;left:0;top:200px;width:1200px}
.quote-mark{left:578px;top:258px;font-size:80px;font-weight:700;line-height:1;color:var(--white)}
.testimonial-text{left:180px;top:318px;width:840px;font-size:20px;line-height:38px;text-align:center}
.testimonial-name{left:0;top:448px;width:1200px;text-align:center;font-size:17px;font-weight:700}

/* blog */
.blog-title{left:0;top:3580px;width:1200px}
.post{top:3653px;width:328px}
.post-image{height:190px}
.post-date{position:absolute;left:14px;top:172px;background:var(--orange);font-size:12px;font-weight:600;padding:6px 10px}
.post h3{font-size:19px;font-weight:500;text-transform:uppercase;margin-top:38px}
.post p{font-size:12.5px;line-height:25px;color:var(--muted);margin-top:6px}
.post .more{font-size:13px;font-weight:700;margin-top:6px;display:block}

/* footer */
.site-footer{left:0;top:4115px;width:1200px;height:560px}
.footer-photo{position:absolute;inset:0;background:linear-gradient(180deg,#2a2f35 0%,#23272b 60%,#1c1e20 100%)}
.footer-brand{left:0;top:80px;width:1200px;text-align:center}
.footer-square{width:80px;height:80px;background:var(--white);margin:0 auto}
.footer-name{font-size:36px;color:var(--orange);margin-top:8px;letter-spacing:1px}
.contact{top:245px;width:300px;text-align:center;font-size:17px;line-height:28px}
.contact-icon{width:82px;height:82px;border-radius:50%;background:var(--orange);margin:0 auto 14px;display:flex;align-items:center;justify-content:center}
.footer-links{left:0;top:422px;width:1200px;text-align:center;font-size:16px}
.footer-links a{color:var(--white);text-decoration:none}
.copyright{left:0;top:462px;width:1200px;text-align:center;font-size:14px;color:var(--muted)}
.socials{left:538px;top:502px;display:flex;gap:10px}
.socials span{width:32px;height:32px;border-radius:50%;border:2px solid var(--white)}
</style>
</head>
<body>

<header class="site-header abs">
  <div class="support abs">
    <div class="support-icon">
      <svg width="22" height="22" viewBox="0 0 24 24"><path fill="#f15a22" d="M6.6 10.8a15 15 0 0 0 6.6 6.6l2.2-2.2a1 1 0 0 1 1-.25 11.4 11.4 0 0 0 3.6.57 1 1 0 0 1 1 1V20a1 1 0 0 1-1 1A17 17 0 0 1 3 4a1 1 0 0 1 1-1h3.5a1 1 0 0 1 1 1c0 1.25.2 2.45.57 3.57a1 1 0 0 1-.25 1z"/></svg>
    </div>
    <div>
      <div class="support-label">Support Call us</div>
      <div class="support-number">1-800-555-0142</div>
    </div>
  </div>
  <div class="brand abs"><span class="brand-square"></span><span class="brand-name">VALDROME</span></div>
  <a class="btn header-cta abs" href="#">
    <svg width="16" height="16" viewBox="0 0 24 24"><rect x="3" y="5" width="18" height="16" fill="none" stroke="#fff" stroke-width="2.5"/><path d="M3 10h18M8 2v5M16 2v5" stroke="#fff" stroke-width="2.5"/></svg>
    Book an appointment
  </a>
</header>

<nav class="main-nav abs">
  <a href="#">Home</a><a href="#">About Us</a><a href="#">Our Services</a><a href="#">Our Approach</a><a href="#">Testimonials</a><a href="#">Contact Us</a>
</nav>

<section class="hero abs">
  <div class="hero-photo" role="img" aria-label="Photo of a designer sketching brand concepts at a desk beside a monitor"></div>
  <div class="hero-copy abs">
    <h1>VALDROME</h1>
    <h2>A Specialized Brand Consultancy.</h2>
    <p>We help our clients identify and develop protectable source identifiers through asset creation-oriented strategies.</p>
    <a class="btn hero-cta" href="#">
      <svg width="16" height="16" viewBox="0 0 24 24"><rect x="3" y="5" width="18" height="16" fill="none" stroke="#fff" stroke-width="2.5"/><path d="M3 10h18M8 2v5M16 2v5" stroke="#fff" stroke-width="2.5"/></svg>
      Book an appointment
    </a>
  </div>
  <svg class="abs" style="left:0;bottom:0" width="1200" height="90" viewBox="0 0 1200 90" preserveAspectRatio="none">
    <path d="M0 60 C300 10 700 95 1200 40 L1200 90 L0 90Z" fill="#4a4a4a"/>
    <path d="M0 60 C300 10 700 95 1200 40 L1200 50 C700 105 300 22 0 72Z" fill="#f15a22"/>
  </svg>
</section>

<div class="about-visual abs" role="img" aria-label="Illustration of a brand concept sketch with loading bar and surrounding notes"></div>
<div class="about-copy abs">
  <h2>About Us</h2>
  <p>Sed ut perspiciatis unde omnis iste natus error sit voluptatem accusantium doloremque laudantium, totam rem aperiam, eaque ipsa quae ab illo inventore veritatis et quasi architecto beatae vitae dicta sunt explicabo. Nemo enim ipsam voluptatem quia voluptas sit aspernatur aut odit aut fugit, sed quia consequuntur magni dolores eos qui ratione voluptatem sequi nesciunt.</p>
  <a class="btn about-cta" href="#">Read More</a>
</div>

<section class="services abs">
  <div class="services-photo" role="img" aria-label="Dark photo of a chalkboard with brand, strategy and marketing sketches"></div>
  <svg class="abs" style="left:0;top:0" width="1200" height="70" viewBox="0 0 1200 70" preserveAspectRatio="none"><path d="M0 0 H1200 V20 C800 70 400 -10 0 40Z" fill="#4a4a4a"/><path d="M600 45 C850 40 1050 20 1200 10 V16 C1050 28 850 48 600 45Z" fill="#f15a22"/></svg>
  <h2 class="section-title">Our Services</h2>
  <p class="lede">At vero eos et accusamus et iusto odio dignissimos ducimus qui blanditiis praesentium voluptatum deleniti atque corrupti quos dolores et quas molestias excepturi sint</p>
  <svg class="abs" style="left:0;bottom:0" width="1200" height="90" viewBox="0 0 1200 90" preserveAspectRatio="none"><path d="M0 70 C400 10 800 90 1200 30 V90 H0Z" fill="#4a4a4a"/><path d="M0 70 C200 40 400 28 520 30 C400 36 200 52 0 78Z" fill="#f15a22"/></svg>
</section>

<svg class="slider-arrow abs" style="left:40px;top:1822px" viewBox="0 0 44 30"><path d="M42 15H4M16 3 4 15l12 12" fill="none" stroke="#fff" stroke-width="3"/></svg>
<svg class="slider-arrow abs" style="left:1118px;top:1822px" viewBox="0 0 44 30"><path d="M2 15h38M28 3l12 12-12 12" fill="none" stroke="#fff" stroke-width="3"/></svg>

<article class="service-card abs" style="left:90px">
  <svg width="70" height="70" viewBox="0 0 70 70"><circle cx="28" cy="28" r="16" fill="none" stroke="#f15a22" stroke-width="4"/><path d="M40 40 60 60" stroke="#f15a22" stroke-width="6"/><path d="M20 28h16M28 20v16" stroke="#f15a22" stroke-width="2"/></svg>
  <h3>Brand Research</h3>
  <p>Sed ut perspiciatis unde omnis iste natus error sit voluptatem accusantium doloremque laudantium</p>
  <a class="more">Read More &rarr;</a>
</article>
<article class="service-card abs" style="left:440px">
  <svg width="70" height="70" viewBox="0 0 70 70"><circle cx="35" cy="35" r="26" fill="none" stroke="#f15a22" stroke-width="4"/><path d="M20 50 50 20M42 20h8v8M22 22l8 8M30 22l-8 8M42 42l8 8M50 42l-8 8" stroke="#f15a22" stroke-width="3" fill="none"/></svg>
  <h3>Brand Strategy</h3>
  <p>Sed ut perspiciatis unde omnis iste natus error sit voluptatem accusantium doloremque laudantium</p>
  <a class="more">Read More &rarr;</a>
</article>
<article class="service-card abs" style="left:788px">
  <svg width="70" height="70" viewBox="0 0 70 70"><rect x="8" y="12" width="54" height="40" fill="none" stroke="#f15a22" stroke-width="4"/><path d="M16 44l12-12 8 8 16-16M35 52v8M24 62h22" stroke="#f15a22" stroke-width="4" fill="none"/></svg>
  <h3>Brand Management</h3>
  <p>Sed ut perspiciatis unde omnis iste natus error sit voluptatem accusantium doloremque laudantium</p>
  <a class="more">Read More &rarr;</a>
</article>

<h2 class="section-title approach-title abs">Our Approach</h2>
<p class="lede approach-lede abs">Sed ut perspiciatis unde omnis iste natus error sit voluptatem accusantium doloremque laudantium, totam rem aperiam, eaque ipsa quae ab illo inventore veritatis et quasi architecto beatae vitae dicta sunt explicabo. Nemo enim ipsam voluptatem quia voluptas sit aspernatur aut odit aut fugit, sed quia consequuntur magni dolores eos qui ratione voluptatem sequi nesciunt.</p>

<div class="step abs" style="left:89px">
  <div class="step-ring"><div><svg width="90" height="90" viewBox="0 0 90 90"><path d="M8 45C22 24 68 24 82 45 68 66 22 66 8 45Z" fill="none" stroke="#fff" stroke-width="4"/><circle cx="45" cy="45" r="12" fill="none" stroke="#fff" stroke-width="4"/><circle cx="45" cy="45" r="4" fill="#fff"/></svg></div></div>
  <div class="step-label">Envision</div>
</div>
<div class="step abs" style="left:348px">
  <div class="step-ring"><div><svg width="90" height="90" viewBox="0 0 90 90"><path d="M20 70 48 42M40 34l16 16 14-30Z" fill="none" stroke="#fff" stroke-width="5" stroke-linejoin="round"/><path d="M66 12v8M78 24h-8M74 16l-6 6" stroke="#fff" stroke-width="3"/></svg></div></div>
  <div class="step-label">Explore</div>
</div>
<div class="step abs" style="left:609px">
  <div class="step-ring"><div><svg width="90" height="90" viewBox="0 0 90 90"><rect x="14" y="14" width="62" height="48" fill="none" stroke="#fff" stroke-width="4"/><path d="M26 52V38M38 52V28M50 52V34M62 52V24M45 62v10M30 76h30" stroke="#fff" stroke-width="5"/></svg></div></div>
  <div class="step-label">Evaluate</div>
</div>
<div class="step abs" style="left:871px">
  <div class="step-ring"><div><svg width="90" height="90" viewBox="0 0 90 90"><rect x="12" y="16" width="66" height="50" fill="none" stroke="#fff" stroke-width="4"/><circle cx="45" cy="41" r="12" fill="none" stroke="#fff" stroke-width="4"/><path d="M45 23v6M45 53v6M27 41h6M57 41h6M33 73h24" stroke="#fff" stroke-width="4"/></svg></div></div>
  <div class="step-label">Execute</div>
</div>

<section class="testimonials abs">
  <div class="testimonials-photo" role="img" aria-label="Photo of a designer's hand sketching on paper beside a keyboard and colour swatches"></div>
  <svg class="abs" style="left:0;top:0" width="1200" height="90" viewBox="0 0 1200 90" preserveAspectRatio="none"><path d="M0 0H1200V40C800 90 400 10 0 60Z" fill="#4a4a4a"/><path d="M650 50C900 55 1050 35 1200 20V28C1050 45 900 62 650 50Z" fill="#f15a22"/></svg>
  <h2 class="section-title">Testimonials</h2>
  <div class="quote-mark abs">&ldquo;</div>
  <p class="testimonial-text abs">Sed ut perspiciatis unde omnis iste natus error sit voluptatem accusantium doloremque laudantium, totam rem aperiam, eaque ipsa quae ab illo inventore veritatis et quasi architecto beatae vitae dicta sunt explicabo.</p>
  <div class="testimonial-name abs">Marta Olsen</div>
  <svg class="abs" style="left:68px;top:330px" width="66" height="40" viewBox="0 0 66 40"><path d="M64 20H6M24 3 6 20l18 17" fill="none" stroke="#fff" stroke-width="4"/></svg>
  <svg class="abs" style="left:1066px;top:330px" width="66" height="40" viewBox="0 0 66 40"><path d="M2 20h58M42 3l18 17-18 17" fill="none" stroke="#fff" stroke-width="4"/></svg>
  <svg class="abs" style="left:0;bottom:0" width="1200" height="100" viewBox="0 0 1200 100" preserveAspectRatio="none"><path d="M0 70C400 100 800 20 1200 50V100H0Z" fill="#4a4a4a"/><path d="M0 62C300 90 500 84 700 70 500 92 300 98 0 74Z" fill="#f15a22"/></svg>
</section>

<h2 class="section-title blog-title abs">Our Blog</h2>
<article class="post abs" style="left:87px">
  <div class="post-image" role="img" aria-label="Photo of a logo sketch on a desk" style="background:linear-gradient(135deg,#a8a29a,#d9d5cf 60%,#8c8780)"></div>
  <span class="post-date">Oct 27 2018</span>
  <h3>Sed ut perspiciatis unde</h3>
  <p>Sed ut perspiciatis unde omnis iste natus error sit voluptatem accusantium doloremque laudantium, totam rem aperiam, eaque ipsa quae ab illo</p>
  <a class="more">Read More</a>
</article>
<article class="post abs" style="left:433px">
  <div class="post-image" role="img" aria-label="Photo of a creative team workspace" style="background:linear-gradient(135deg,#4d6273,#9aa7b1 55%,#c9b9a4)"></div>
  <span class="post-date">Oct 27 2018</span>
  <h3>Sed ut perspiciatis unde</h3>
  <p>Sed ut perspiciatis unde omnis iste natus error sit voluptatem accusantium doloremque laudantium, totam rem aperiam, eaque ipsa quae ab illo</p>
  <a class="more">Read More</a>
</article>
<article class="post abs" style="left:779px">
  <div class="post-image" role="img" aria-label="Photo of hands drawing wireframes on paper" style="background:linear-gradient(135deg,#d8d8d8,#f1f1f1 50%,#a9a9a9)"></div>
  <span class="post-date">Oct 27 2018</span>
  <h3>Sed ut perspiciatis unde</h3>
  <p>Sed ut perspiciatis unde omnis iste natus error sit voluptatem accusantium doloremque laudantium, totam rem aperiam, eaque ipsa quae ab illo</p>
  <a class="more">Read More</a>
</article>

<footer class="site-footer abs">
  <div class="footer-photo" role="img" aria-label="Dark photo of a small team at work in an office"></div>
  <svg class="abs" style="left:0;top:0" width="1200" height="60" viewBox="0 0 1200 60" preserveAspectRatio="none"><path d="M0 0H1200V20C800 60 400 0 0 30Z" fill="#4a4a4a"/></svg>
  <div class="footer-brand abs">
    <div class="footer-square"></div>
    <div class="footer-name">VALDROME</div>
  </div>
  <div class="contact abs" style="left:150px">
    <div class="contact-icon"><svg width="36" height="36" viewBox="0 0 24 24"><path d="M12 2a7 7 0 0 0-7 7c0 5 7 13 7 13s7-8 7-13a7 7 0 0 0-7-7Z" fill="none" stroke="#fff" stroke-width="2"/><circle cx="12" cy="9" r="2.5" fill="none" stroke="#fff" stroke-width="2"/></svg></div>
    48 Larkmoor Lane,<br>Brindle Falls, VA 22990
  </div>
  <div class="contact abs" style="left:450px">
    <div class="contact-icon"><svg width="34" height="34" viewBox="0 0 24 24"><path fill="#fff" d="M6.6 10.8a15 15 0 0 0 6.6 6.6l2.2-2.2a1 1 0 0 1 1-.25 11.4 11.4 0 0 0 3.6.57 1 1 0 0 1 1 1V20a1 1 0 0 1-1 1A17 17 0 0 1 3 4a1 1 0 0 1 1-1h3.5a1 1 0 0 1 1 1c0 1.25.2 2.45.57 3.57a1 1 0 0 1-.25 1z"/></svg></div>
    Phone:<br>800 555 0142
  </div>
  <div class="contact abs" style="left:756px">
    <div class="contact-icon"><svg width="36" height="36" viewBox="0 0 24 24"><rect x="3" y="5" width="18" height="14" fill="none" stroke="#fff" stroke-width="2"/><path d="M3 6l9 7 9-7" fill="none" stroke="#fff" stroke-width="2"/></svg></div>
    Email:<br>hello@valdrome.example
  </div>
  <div class="footer-links abs"><a href="#">Home</a> | <a href="#">About Us</a> | <a href="#">Our Services</a> | <a href="#">Our Approach</a> | <a href="#">Blog</a> | <a href="#">Testimonials</a> | <a href="#">Contact Us</a></div>
  <div class="copyright abs">&copy; 2019 Company Name. All right reserved</div>
  <div class="socials abs"><span></span><span></span><span></span><span></span></div>
</footer>

</body>
</html>
```